Business Card Design Project

I would like to have a project of business card with incorporated attachted logo elements in warm colors like: gold, yellow, brown.
We would like incorporate below information into the design
Name of the Company: Continental Hoop Invitational
Name: Dorian Pelkey
Position: Project Director
e-mail: dorian@hoopinvitational.net
mobile: +65 83147092
website: www.hoopinvitational.net
Address: 47 Marbury Lane, #06-11, Singapore 915274
There is a picture attachted which can be used as a back side of the buisness card - we would like to follow the colors theme on the front card ( with the person contact details) how ever the front card we will prefer with white background but with graphfic elements coming from logo.
Project Deadline Extended
Reason: the project has been launched on 24 of April with deadline by 24 of April by mistakes. Thats why I would like to extend the deadline.
Name: Dorian Pelkey
mobile: +65 83147092

```html
<!DOCTYPE html>
<html lang="en">
<head>
<meta charset="utf-8">
<title>Continental Hoop Invitational – Business Card</title>
<link rel="stylesheet" href="https://fonts.googleapis.com/css2?family=Amaranth:ital,wght@0,700;1,400&family=Ubuntu:wght@400;500&display=swap">
<style>
  :root {
    --backdrop: #ece7df;
    --card-white: #ffffff;
    --ink: #111111;
    --gold-1: #d1c01c;
    --gold-2: #b3a823;
    --olive-1: #9a912a;
    --olive-2: #827b2f;
    --olive-3: #6d6832;
    --brand-purple: #6a2b8f;
    --back-dark: #1a120b;
    --back-brown: #3b2816;
    --back-gold: #c9982a;
    --photo-skin: #b89470;
    --photo-shadow: #2a2018;
  }
  * { margin: 0; padding: 0; box-sizing: border-box; }
  html, body { width: 1200px; height: 900px; overflow: hidden; }
  body {
    background: var(--backdrop);
    position: relative;
    font-family: "Ubuntu", sans-serif;
  }
  .card {
    position: absolute;
    top: 300px;
    width: 540px;
    height: 300px;
    overflow: hidden;
    box-shadow: 0 6px 18px rgba(0,0,0,0.25);
  }
  .card--front { left: 40px; background: var(--card-white); }
  .card--back  { left: 620px; background: var(--back-dark); }

  .front__arcs { position: absolute; inset: 0; }

  .brand {
    position: absolute;
    left: 28px;
    top: 218px;
    width: 180px;
    display: flex;
    align-items: center;
    gap: 8px;
    color: var(--brand-purple);
    font-family: "Ubuntu", sans-serif;
    font-weight: 500;
    font-size: 14px;
    line-height: 1.15;
    text-transform: uppercase;
  }
  .brand__dot {
    flex: none;
    width: 16px; height: 16px;
    border-radius: 50%;
    background: var(--brand-purple);
  }

  .identity {
    position: absolute;
    right: 110px;
    top: 40px;
    text-align: right;
    color: var(--ink);
    font-family: "Amaranth", sans-serif;
  }
  .identity__name { font-weight: 700; font-size: 25px; line-height: 1; text-align: left; }
  .identity__role { font-style: italic; font-size: 19px; margin-top: 2px; }

  .online {
    position: absolute;
    right: 26px;
    top: 118px;
    text-align: right;
    font-size: 14.5px;
    line-height: 1.25;
    color: var(--ink);
  }
  .postal {
    position: absolute;
    left: 350px;
    top: 210px;
    font-size: 14.5px;
    line-height: 1.35;
    color: var(--ink);
  }

  .back__stage {
    position: absolute;
    inset: 0;
    background:
      radial-gradient(ellipse at 28% 40%, var(--back-brown) 0%, transparent 62%),
      linear-gradient(120deg, #120d08 0%, var(--back-dark) 55%, #2b1d10 100%);
  }
  .back__photo {
    position: absolute;
    left: 215px;
    top: 40px;
    width: 325px;
    height: 260px;
    background:
      radial-gradient(ellipse at 62% 55%, var(--photo-skin) 0%, #8a6a48 28%, transparent 55%),
      radial-gradient(circle at 92% 70%, var(--back-gold) 0%, #8a6420 30%, transparent 58%),
      linear-gradient(160deg, var(--photo-shadow) 0%, #4a3520 60%, #6a4c22 100%);
  }
</style>
</head>
<body>

<section class="card card--front" aria-label="Business card, front">
  <svg class="front__arcs" width="540" height="300" viewBox="0 0 540 300" aria-hidden="true">
    <circle cx="170" cy="300" r="175" fill="var(--gold-1)"/>
    <circle cx="156" cy="300" r="160" fill="var(--gold-2)"/>
    <circle cx="143" cy="300" r="146" fill="var(--olive-1)"/>
    <circle cx="131" cy="300" r="133" fill="var(--olive-2)"/>
    <circle cx="121" cy="300" r="121" fill="var(--olive-3)"/>
    <circle cx="112" cy="292" r="110" fill="var(--card-white)"/>
  </svg>

  <div class="brand">
    <span class="brand__dot"></span>
    <span class="brand__name">Continental Hoop Invitational</span>
  </div>

  <div class="identity">
    <p class="identity__name">Dorian Pelkey</p>
    <p class="identity__role">Project Director</p>
  </div>

  <div class="online">
    <p>dorian@hoopinvitational.net</p>
    <p>www.hoopinvitational.net</p>
  </div>

  <div class="postal">
    <p>Mobile: +65 83147092</p>
    <p>47 Marbury Lane, #06-11,</p>
    <p>Singapore 915274</p>
  </div>
</section>

<section class="card card--back" aria-label="Business card, back">
  <div class="back__stage"></div>
  <div class="back__photo" role="img" aria-label="Photograph of a performer in motion on a golden pole, lit warmly against a dark brown and gold stage backdrop"></div>
</section>

</body>
</html>
```